Quill Harbor Gems Website revamp

Hi,

We need a working WordPress theme, not just a .PSD file. Thank you.

We need a complete revamp of our website. We sell lab grown diamonds online. We sell the idea that everyone should be able to afford a diamond. Thus our diamonds are priced very reasonably. Our selling point "the joy of giving and receiving a diamond in a little box".

Our range of products includes rings, bangles, necklace, ear rings etc. We currently only operate in Singapore. Some photos of our products are on our websites.

Need.
- Clean look and feel, simplistic preferably white and soft colours
- Easy to navigate
- No banners
- E Com
- Introduction page
- Willing to change logo if needed

Existing page: www.quillharborgems-example.com

Target Market(s)

Young ladies
Ladies
Men buying for ladies
Young boyfriends fresh out of school buying for love ones
Working ladies to match what they wear to work

Industry/Entity Type

Online

Requirements
Must have
• ECOM. Product shopping cart
Pictures uploads
Intro page
Nice to have
• Pastel colors preferred. - Color scheme is important in our business to create a long term impression. Color scheme will also be used for next potential project, i.e. packaging design.

Should not have
• Should not have old style fonts.

```html
<!DOCTYPE html>
<html lang="en">
<head>
<meta charset="utf-8">
<title>Eternity – Quill Harbor Gems</title>
<link rel="stylesheet" href="https://fonts.googleapis.com/css2?family=PT+Sans:wght@400;700&family=Montserrat:wght@600;700&display=swap">
<style>
:root{
  --ink:#2b2b2b;
  --text:#555;
  --muted:#888;
  --accent:#ee5a2e;
  --accent-soft:#f47a4e;
  --blue:#6f93c4;
  --topbar:#2e2e2e;
  --header-bg:#f3f3f3;
  --line:#e2e2e2;
  --footer-bg:#f5f5f5;
  --footer-dark:#ececec;
  --sapphire:#2a3a6e;
  --silver:#d9dbe0;
  --white:#fff;
}
*{box-sizing:border-box;margin:0;padding:0}
html,body{width:1200px;height:2857px;overflow:hidden}
body{position:relative;background:var(--white);font-family:"PT Sans",Arial,sans-serif;color:var(--text);font-size:14px}
.abs{position:absolute}
.topbar{left:0;top:0;width:1200px;height:29px;background:var(--topbar)}
.topbar a{position:absolute;top:7px;color:#ddd;font-size:12px;text-decoration:none}
.header{left:0;top:29px;width:1200px;height:238px;background:var(--header-bg)}
.brand{left:52px;top:60px;width:240px;height:140px;display:flex;align-items:center;gap:12px}
.brand-mark{width:30px;height:30px;border-radius:50%;background:var(--accent);flex:none}
.brand-name{font-size:24px;font-weight:400;color:var(--ink);line-height:1.15}
.welcome{left:312px;top:80px;font-size:14px;color:var(--ink)}
.welcome a{color:var(--ink)}
.search{left:805px;top:66px;width:232px;height:44px;background:var(--white);border-radius:22px;padding:11px 18px;color:#aaa;font-size:14px}
.search-btn{left:996px;top:64px;width:46px;height:46px;border-radius:50%;background:var(--blue)}
.cart-btn{left:1048px;top:64px;width:46px;height:46px;border-radius:50%;background:var(--accent)}
.cart-label{left:1102px;top:78px;font-weight:700;font-size:14px;color:var(--ink)}
.nav{left:312px;top:162px;display:flex;gap:38px;font-family:"Montserrat",Arial,sans-serif;font-weight:700;font-size:16px;color:var(--ink)}
.nav-rule{left:312px;top:200px;width:870px;height:2px;background:var(--line)}
.breadcrumb{left:24px;top:234px;font-size:14px;color:var(--ink)}
.page-title{left:24px;top:344px;font-size:32px;font-weight:400;color:var(--ink);letter-spacing:1px}
.title-rule{left:24px;top:408px;width:1152px;height:2px;background:var(--line)}
.product-photo{left:24px;top:464px;width:464px;height:584px;border:1px solid var(--line);background:radial-gradient(circle at 50% 48%,var(--sapphire) 0 9%,var(--silver) 10% 34%,var(--white) 36%)}
.thumb{top:1076px;width:91px;height:91px;border:1px solid var(--line)}
.thumb-a{left:52px;background:radial-gradient(circle,var(--sapphire) 0 16%,var(--silver) 18% 42%,var(--white) 46%)}
.thumb-b{left:157px;background:radial-gradient(circle,#b8a2d6 0 16%,var(--silver) 18% 42%,var(--white) 46%)}
.review-link{left:517px;top:474px;font-size:12px;color:var(--blue);text-transform:uppercase}
.about{left:517px;top:516px;font-size:15px;color:var(--ink);line-height:1.35}
.rule-a{left:517px;top:657px;width:660px;height:1px;background:var(--line)}
.price{left:517px;top:680px;font-size:40px;color:var(--accent-soft)}
.rule-b{left:517px;top:757px;width:660px;height:1px;background:var(--line)}
.qty{left:517px;top:786px;width:116px;height:43px;border:1px solid #ccc;padding:11px 12px;font-size:14px;color:var(--ink)}
.add-to-cart{left:657px;top:786px;width:164px;height:43px;border-radius:22px;background:var(--accent);color:var(--white);font-weight:700;font-size:14px;display:flex;align-items:center;justify-content:center;gap:10px;text-transform:uppercase}
.compare{left:850px;top:790px;display:flex;align-items:center;gap:12px;font-size:12px;color:var(--ink);text-transform:uppercase}
.compare-icon{width:34px;height:34px;border-radius:50%;background:#eef0f3;display:flex;align-items:center;justify-content:center}
.tabs{left:36px;top:1219px;display:flex;gap:6px}
.tab{height:42px;padding:0 22px;border:1px solid var(--line);border-bottom:none;font-size:13px;color:var(--text);display:flex;align-items:center;text-transform:uppercase;background:#fafafa}
.tab.active{color:var(--accent);border-color:#bcd0e6;background:var(--white)}
.tabs-rule{left:24px;top:1260px;width:1168px;height:2px;background:#d6e2ef}
.section-heading{font-size:24px;color:var(--ink);text-transform:uppercase}
.desc-heading{left:34px;top:1297px}
.related-heading{left:34px;top:1634px}
.related-rule{left:24px;top:1700px;width:1152px;height:1px;background:var(--line)}
.card{top:1755px;width:268px;height:400px;border:1px solid var(--line);box-shadow:0 2px 6px rgba(0,0,0,.06);background:var(--white)}
.card-1{left:30px}.card-2{left:321px}
.card-photo{position:absolute;left:14px;top:18px;width:240px;height:226px}
.card-photo.sapphire{background:radial-gradient(circle at 50% 48%,var(--sapphire) 0 10%,var(--silver) 12% 38%,var(--white) 42%)}
.card-photo.band{background:radial-gradient(ellipse 45% 22% at 50% 50%,var(--silver) 0 70%,var(--white) 100%)}
.card-name{position:absolute;left:0;width:100%;top:270px;text-align:center;font-size:16px;color:var(--ink);text-transform:uppercase}
.card-rule{position:absolute;left:20px;right:20px;top:320px;height:1px;background:var(--line)}
.card-dot{position:absolute;left:50%;top:317px;width:6px;height:6px;margin-left:-3px;border-radius:50%;background:#ccc}
.card-price{position:absolute;left:0;width:100%;top:350px;text-align:center;font-size:18px;color:var(--accent-soft)}
.footer{left:0;top:2464px;width:1200px;height:393px;background:var(--footer-bg)}
.footer-col{top:2526px;width:270px}
.footer-col h3{font-size:20px;font-weight:400;color:var(--ink);text-transform:uppercase;padding-bottom:10px;border-bottom:1px solid var(--line);margin-bottom:24px}
.footer-col li{list-style:none;font-size:14px;color:var(--ink);line-height:29px}
.col-1{left:24px}.col-2{left:319px}.col-3{left:614px}.col-4{left:910px}
.contact-item{display:flex;gap:12px;font-size:14px;color:var(--ink);line-height:1.35;margin-bottom:10px}
.contact-item svg{flex:none;margin-top:3px}
.newsletter-band{left:0;top:2738px;width:880px;height:119px}
.news-icon{left:24px;top:2760px;width:46px;height:46px;border-radius:50%;background:var(--accent)}
.news-title{left:80px;top:2770px;font-size:22px;color:var(--ink)}
.news-copy{left:208px;top:2775px;font-size:14px;color:var(--ink)}
.news-input{left:581px;top:2762px;width:264px;height:44px;border:1px solid #ccc;border-radius:22px;background:var(--white);padding:12px 20px;font-size:13px;color:var(--ink)}
.payments{left:880px;top:2738px;width:320px;height:119px;background:var(--footer-dark)}
.pay-card{top:2768px;width:62px;height:38px;border-radius:5px;background:var(--white);border:1px solid #ddd}
</style>
</head>
<body>

<div class="abs topbar"><a style="left:1014px">My Account</a><a style="left:1110px">Contact Us</a></div>

<header class="abs header"></header>
<div class="abs brand"><span class="brand-mark"></span><span class="brand-name">Quill Harbor Gems</span></div>
<p class="abs welcome">Welcome visitor you can <a>login</a> or <a>create an account</a>.</p>
<div class="abs search">Search</div>
<div class="abs search-btn"><svg width="46" height="46" viewBox="0 0 46 46"><circle cx="21" cy="21" r="7" fill="none" stroke="#fff" stroke-width="2.5"/><line x1="26" y1="26" x2="31" y2="31" stroke="#fff" stroke-width="2.5"/></svg></div>
<div class="abs cart-btn"><svg width="46" height="46" viewBox="0 0 46 46"><path d="M14 19h18l-2 10H16z" fill="#fff"/><path d="M18 19l5-6 5 6" fill="none" stroke="#fff" stroke-width="2"/></svg></div>
<div class="abs cart-label">CART £0</div>
<nav class="abs nav"><span>HOME</span><span>OUR STORY</span><span>OUR DIAMONDS</span><span>SHOP</span><span>CONTACT US</span></nav>
<div class="abs nav-rule"></div>
<div class="abs breadcrumb">Home / SHOP / ETERNITY</div>

<h1 class="abs page-title">ETERNITY</h1>
<div class="abs title-rule"></div>

<div class="abs product-photo" role="img" aria-label="Product photo: white gold ring with oval sapphire surrounded by diamonds"></div>
<div class="abs thumb thumb-a" role="img" aria-label="Thumbnail: sapphire ring"></div>
<div class="abs thumb thumb-b" role="img" aria-label="Thumbnail: ring with pink stone"></div>

<div class="abs review-link">Add your review</div>
<div class="abs about">ABOUT ETERNITY<br>A ring that is Eternity, for the one you love most.</div>
<div class="abs rule-a"></div>
<div class="abs price">£38.87</div>
<div class="abs rule-b"></div>
<div class="abs qty">1</div>
<div class="abs add-to-cart"><svg width="16" height="14" viewBox="0 0 16 14"><path d="M1 5h14l-2 8H3z" fill="#fff"/><path d="M4 5l4-4 4 4" fill="none" stroke="#fff" stroke-width="1.6"/></svg>Add to cart</div>
<div class="abs compare"><span class="compare-icon"><svg width="16" height="14" viewBox="0 0 16 14"><path d="M2 4h11M10 1l3 3-3 3M14 10H3M6 7l-3 3 3 3" fill="none" stroke="#666" stroke-width="1.4"/></svg></span>Compare this</div>

<div class="abs tabs">
  <div class="tab active">Description</div>
  <div class="tab">Additional information</div>
  <div class="tab">Technical details</div>
  <div class="tab">Reviews (0)</div>
</div>
<div class="abs tabs-rule"></div>

<h2 class="abs section-heading desc-heading">Product description</h2>

<h2 class="abs section-heading related-heading">Related products</h2>
<div class="abs related-rule"></div>

<article class="abs card card-1">
  <div class="card-photo sapphire" role="img" aria-label="Product photo: sapphire and diamond ring"></div>
  <div class="card-name">Eternity</div><div class="card-rule"></div><div class="card-dot"></div>
  <div class="card-price">£31.96</div>
</article>
<article class="abs card card-2">
  <div class="card-photo band" role="img" aria-label="Product photo: diamond eternity band"></div>
  <div class="card-name">Pink</div><div class="card-rule"></div><div class="card-dot"></div>
  <div class="card-price">£31.96</div>
</article>

<footer class="abs footer"></footer>
<div class="abs footer-col col-1">
  <h3>Contact us</h3>
  <div class="contact-item"><svg width="12" height="16" viewBox="0 0 12 16"><path d="M6 0a6 6 0 0 1 6 6c0 4-6 10-6 10S0 10 0 6a6 6 0 0 1 6-6z" fill="var(--blue)"/><circle cx="6" cy="6" r="2" fill="#fff"/></svg><span>27 Harbour Lane,<br>#03-B2 Marina Arcade,<br>Singapore 018900</span></div>
  <div class="contact-item"><svg width="14" height="14" viewBox="0 0 14 14"><path d="M3 0l3 3-2 2c1 2 3 4 5 5l2-2 3 3-2 3C6 14 0 8 0 3z" fill="var(--blue)"/></svg><span>+65 9000 1234</span></div>
  <div class="contact-item"><svg width="14" height="12" viewBox="0 0 14 12"><rect width="14" height="11" rx="1" fill="var(--blue)"/><path d="M1 1l6 5 6-5" fill="none" stroke="#fff" stroke-width="1.2"/></svg><span>info@quillharborgems-example.com</span></div>
</div>
<div class="abs footer-col col-2"><h3>Information</h3><ul><li>Sample Page</li><li>Contact Us</li><li>News</li></ul></div>
<div class="abs footer-col col-3"><h3>Customer service</h3><ul><li>Checkout</li><li>Cart</li><li>Privacy Policy</li></ul></div>
<div class="abs footer-col col-4"><h3>My account</h3><ul><li>My Account</li><li>Edit My Address</li><li>Logout</li><li>Lost Password</li></ul></div>

<div class="abs news-icon"><svg width="46" height="46" viewBox="0 0 46 46"><rect x="14" y="16" width="18" height="14" rx="1" fill="#fff"/><path d="M14 17l9 7 9-7" fill="none" stroke="var(--accent)" stroke-width="1.5"/></svg></div>
<div class="abs news-title">Newsletter</div>
<div class="abs news-copy">Subscribe to notifications about discounts from our store</div>
<div class="abs news-input">Email<svg class="abs" style="right:16px;top:14px" width="10" height="16" viewBox="0 0 10 16"><path d="M2 2l6 6-6 6" fill="none" stroke="#555" stroke-width="1.6"/></svg></div>

<div class="abs payments"></div>
<div class="abs pay-card" style="left:907px"></div>
<div class="abs pay-card" style="left:975px"></div>
<div class="abs pay-card" style="left:1043px"></div>
<div class="abs pay-card" style="left:1111px"></div>

</body>
</html>
```